Water Filter Company Needs Bizz Cards!!

Need business cards for my company. We sell whole home water filters and salt free water softeners. No more buying bottled water. Our filtering units filter out all heavy metals, chlorine, and VOC's, last 15 years, and are maintenance free and supply your whole home with spring quality alkaline water. Our Salt free water conditioners, eliminate hard water and scale, without lowering the ph, or TDS's (total Dissolved solids)

I think this is the color code we are using on my site. My logo looks good behind it. #192841

Website will be www.Brovexa.com

Industry/Entity Type

Water Purification

Contact Information for Business Card

For now, just insert standard Dummy text. I need these text lines for the info to be editable so i can make them for multiple employees. I do have Photoshop and illustrator, unless there is a simpler program i can use solely for biz cards

Font styles to use
Sans Serif

Requirements
Must have
• Use my preexisting logo.

www.BroVexa.com

Spring Quality Alkaline Water at every tap.

List out services. Whole Home Water Filters, Salt Free Water Softeners, Clarimont KT7, UV Sterilizers
Nice to have
• I think this is the color code we are using on my site. My logo looks good behind it. #192841 or black. Please no white or light blue backgrounds.

Maybe a picture of my tank.

Slogan like Spring Quality Alkaline Water at every tap.
And just list the services Whole Home Water Filters, Salt Free Water Softeners, Clarimont KT7, UV Sterilizers

I think I would like to not have a contrasting textured logo like I see on some of them. I may use it for my personal cards, but new employees may not want the extra expense.
Should not have
• A different logo than the one provided.

White or baby blue backgrounds. Use the color code, or blacks.

```html
<!DOCTYPE html>
<html lang="en">
<head>
<meta charset="utf-8">
<title>Brovexa Business Cards</title>
<link rel="stylesheet" href="https://fonts.googleapis.com/css2?family=Open+Sans:wght@300;400;600;700;800&display=swap">
<style>
  :root {
    --stage: #1f6c9e;
    --card: #192841;
    --accent: #2aa8e6;
    --accent-deep: #1b86cf;
    --accent-light: #5cc6f2;
    --text: #ffffff;
    --muted: #8a93a3;
  }
  * { margin: 0; padding: 0; box-sizing: border-box; }
  html, body { width: 1200px; height: 900px; overflow: hidden; }
  body {
    background: var(--stage);
    font-family: "Open Sans", sans-serif;
    display: flex;
    flex-direction: column;
    align-items: center;
    justify-content: center;
    gap: 40px;
  }
  .card {
    position: relative;
    width: 700px;
    height: 400px;
    background: var(--card);
    overflow: hidden;
    border-radius: 4px;
    box-shadow: 0 12px 30px rgba(0, 0, 0, 0.35);
  }
  .card__pattern {
    position: absolute;
    inset: 0;
    width: 100%;
    height: 100%;
  }
  .brand {
    display: flex;
    align-items: center;
    gap: 12px;
    color: var(--accent);
    font-weight: 700;
    white-space: nowrap;
  }
  .brand__dot { border-radius: 50%; background: var(--accent); flex: none; }

  .front-content {
    position: absolute;
    left: 330px;
    right: 36px;
    top: 96px;
    display: flex;
    flex-direction: column;
    align-items: center;
    text-align: center;
  }
  .card--front .brand { font-size: 60px; letter-spacing: -1px; line-height: 1.1; }
  .card--front .brand__dot { width: 32px; height: 32px; }
  .slogan {
    margin-top: 14px;
    font-size: 15px;
    font-weight: 600;
    color: var(--text);
    letter-spacing: 0.3px;
  }
  .services {
    margin-top: 18px;
    padding-top: 14px;
    border-top: 1px solid rgba(42, 168, 230, 0.5);
    list-style: none;
    display: grid;
    grid-template-columns: auto auto;
    gap: 8px 26px;
    font-size: 12.5px;
    color: var(--muted);
    text-align: left;
  }
  .services__item { display: flex; align-items: center; gap: 8px; white-space: nowrap; }
  .services__item::before {
    content: "";
    width: 6px; height: 6px;
    background: var(--accent);
    flex: none;
  }

  .card--back .brand {
    position: absolute;
    right: 40px;
    bottom: 40px;
    font-size: 28px;
    letter-spacing: -0.5px;
  }
  .card--back .brand__dot { width: 16px; height: 16px; }

  .person {
    position: absolute;
    left: 290px;
    top: 62px;
    color: var(--text);
  }
  .person__name { font-size: 30px; font-weight: 300; letter-spacing: 1px; text-transform: uppercase; }
  .person__name strong { font-weight: 800; }
  .person__role {
    margin-top: 4px;
    font-size: 17px;
    font-weight: 300;
    letter-spacing: 14px;
    color: var(--muted);
    text-transform: uppercase;
  }
  .contact {
    position: absolute;
    left: 290px;
    top: 180px;
    list-style: none;
    color: var(--text);
    font-size: 15px;
  }
  .contact__item { display: flex; align-items: center; gap: 16px; height: 42px; }
  .contact__icon { width: 22px; height: 22px; flex: none; }
</style>
</head>
<body>

<section class="card card--front">
  <svg class="card__pattern" viewBox="0 0 700 400" role="img" aria-label="Blue mosaic of scattered translucent squares along the left edge">
    <defs>
      <linearGradient id="mosaicFront" x1="0" y1="0" x2="1" y2="1">
        <stop offset="0" stop-color="var(--accent-light)"/>
        <stop offset="0.5" stop-color="var(--accent)"/>
        <stop offset="1" stop-color="var(--accent-deep)"/>
      </linearGradient>
    </defs>
    <polygon points="0,40 120,0 250,0 300,400 0,400" fill="url(#mosaicFront)" opacity="0.9"/>
  </svg>
  <div class="front-content">
    <div class="brand"><span class="brand__dot"></span>Brovexa</div>
    <p class="slogan">Spring Quality Alkaline Water at every tap.</p>
    <ul class="services">
      <li class="services__item">Whole Home Water Filters</li>
      <li class="services__item">Salt Free Water Softeners</li>
      <li class="services__item">Clarimont KT7</li>
      <li class="services__item">UV Sterilizers</li>
    </ul>
  </div>
</section>

<section class="card card--back">
  <svg class="card__pattern" viewBox="0 0 700 400" role="img" aria-label="Blue mosaic of scattered translucent squares along the left edge">
    <defs>
      <linearGradient id="mosaicBack" x1="0" y1="0" x2="1" y2="1">
        <stop offset="0" stop-color="var(--accent-light)"/>
        <stop offset="0.5" stop-color="var(--accent)"/>
        <stop offset="1" stop-color="var(--accent-deep)"/>
      </linearGradient>
    </defs>
    <polygon points="0,0 90,0 250,400 0,400" fill="url(#mosaicBack)" opacity="0.9"/>
  </svg>

  <div class="person">
    <div class="person__name"><strong>Dana</strong> Whitfield</div>
    <div class="person__role">Executive</div>
  </div>

  <ul class="contact">
    <li class="contact__item">
      <svg class="contact__icon" viewBox="0 0 24 24"><path d="M12 2a7 7 0 0 0-7 7c0 5 7 13 7 13s7-8 7-13a7 7 0 0 0-7-7zm0 9.5A2.5 2.5 0 1 1 12 6.5a2.5 2.5 0 0 1 0 5z" fill="#fff"/></svg>
      <span>Riverton, CO, USA</span>
    </li>
    <li class="contact__item">
      <svg class="contact__icon" viewBox="0 0 24 24"><rect x="2" y="5" width="20" height="14" rx="1" fill="#fff"/><path d="M3 6l9 7 9-7" fill="none" stroke="#192841" stroke-width="1.8"/></svg>
      <span>contact@brovexa.com</span>
    </li>
    <li class="contact__item">
      <svg class="contact__icon" viewBox="0 0 24 24"><path d="M6.6 10.8a15 15 0 0 0 6.6 6.6l2.2-2.2a1 1 0 0 1 1-.25 11 11 0 0 0 3.6.6 1 1 0 0 1 1 1V20a1 1 0 0 1-1 1A17 17 0 0 1 3 4a1 1 0 0 1 1-1h3.5a1 1 0 0 1 1 1 11 11 0 0 0 .6 3.6 1 1 0 0 1-.25 1z" fill="#fff"/></svg>
      <span>+123 456 789</span>
    </li>
    <li class="contact__item">
      <svg class="contact__icon" viewBox="0 0 24 24"><circle cx="12" cy="12" r="9.5" fill="#fff"/><g fill="none" stroke="#192841" stroke-width="1.2"><ellipse cx="12" cy="12" rx="4" ry="9.5"/><line x1="2.5" y1="12" x2="21.5" y2="12"/><line x1="4" y1="7.5" x2="20" y2="7.5"/><line x1="4" y1="16.5" x2="20" y2="16.5"/></g></svg>
      <span>www.brovexa.com</span>
    </li>
  </ul>

  <div class="brand"><span class="brand__dot"></span>Brovexa</div>
</section>

</body>
</html>
```